Flyer-Design für Wechseljahres Tag Seminar Vol. 2
Zielgruppe
Seminare, Vorträge , Therapien, Beratung, Coaching
WEchseljahre Beratung
Sexualtherapie, Sexualberatung
Mentaltraining
Es soll Frauen gefallen und ermuntern zum Seminar zu kommen, frü Thema Wechseljahre interessieren
Aufgabenstellung
Grösse A5 Hochkant

```html
<!DOCTYPE html>
<html lang="de">
<head>
<meta charset="utf-8">
<title>Wechseljahre Seminar Vol. 2 – Flyer</title>
<link href="https://fonts.googleapis.com/css2?family=Oswald:wght@200;300;400;500&family=Roboto+Slab:wght@400;700&family=Roboto+Condensed:wght@400;700&family=Merriweather:ital,wght@1,700&display=swap" rel="stylesheet">
<style>
:root{
  --blue:#19a8d3;
  --yellow:#fbe84b;
  --lime:#c6d84c;
  --brown:#6d2b2c;
  --white:#ffffff;
  --ink:#333333;
  --stage:#9a9a9a;
}
*{margin:0;padding:0;box-sizing:border-box}
html,body{width:1200px;height:803px;overflow:hidden;background:var(--stage)}
.canvas{position:relative;width:1200px;height:803px}
.flyer{position:absolute;top:43px;width:511px;height:720px;background:var(--white);overflow:hidden;font-family:"Roboto Condensed","Arial Narrow",sans-serif;color:var(--ink)}
.flyer--front{left:55px}
.flyer--back{left:616px}
.abs{position:absolute}
.slab{font-family:"Roboto Slab",Georgia,serif;font-weight:700}

/* front */
.front-hero{left:0;top:0;width:511px;height:169px;background:linear-gradient(90deg,#bcd8e6 0%,#d6e7ef 45%,#c9b9ad 75%,#b79c8c 100%)}
.front-title{left:26px;top:64px;font-family:"Oswald",sans-serif;font-weight:500;font-size:44px;color:var(--white);letter-spacing:.5px;line-height:1}
.front-sub{left:16px;top:118px;font-family:"Oswald",sans-serif;font-weight:400;font-size:19px;color:var(--white);letter-spacing:.3px;white-space:nowrap}
.vol-badge{left:32px;top:146px;width:62px;height:62px;border-radius:50%;background:var(--yellow);border:3px solid var(--blue);display:flex;align-items:center;justify-content:center;font-family:"Roboto Slab",Georgia,serif;font-weight:700;color:var(--blue);font-size:17px;transform:rotate(-12deg);z-index:2}
.vol-badge b{font-size:28px;margin-left:2px}
.front-portrait{left:0;top:169px;width:276px;height:293px;background:linear-gradient(160deg,#f4f4f4 0%,#d9c6bd 45%,#3aa7c4 75%,#2b2b2b 100%)}
.front-column{left:276px;top:169px;width:235px;height:479px;background:var(--blue);border-top:3px solid var(--yellow);padding:12px 12px 0 14px;display:flex;flex-direction:column}
.front-date{text-align:center;font-family:"Oswald",sans-serif;font-weight:500;font-size:40px;color:var(--yellow);line-height:1.05}
.front-time{margin-top:6px;text-align:center;font-family:"Oswald",sans-serif;font-weight:300;font-size:13px;line-height:1.2;color:var(--white);text-transform:uppercase;white-space:nowrap}
.front-time b{font-weight:400;font-size:20px}
.front-venue{margin-top:3px;text-align:center;font-family:"Oswald",sans-serif;font-weight:300;font-size:12.5px;line-height:1.2;color:var(--white);text-transform:uppercase;white-space:nowrap}
.front-lead{margin-top:14px;font-family:"Roboto Slab",Georgia,serif;font-weight:700;font-size:12.5px;line-height:1.22;color:var(--yellow)}
.front-body{margin-top:8px;font-size:8.2px;line-height:1.38;color:var(--white);text-align:justify}
.front-questions-title{margin-top:12px;font-family:"Roboto Slab",Georgia,serif;font-weight:700;font-size:12.5px;color:var(--yellow)}
.question-list{margin-top:8px;list-style:none;font-size:7.6px;line-height:1.3;color:var(--white)}
.question-list li{position:relative;padding-left:12px;margin-bottom:4px}
.question-list li::before{content:"";position:absolute;left:0;top:1px;width:7px;height:7px;border:1px solid var(--white)}
.front-panel{left:0;top:462px;width:276px;height:186px;background:var(--blue)}
.front-panel-title{left:0;width:276px;top:12px;text-align:center;font-family:"Merriweather",Georgia,serif;font-style:italic;font-weight:700;font-size:15px;line-height:1.3;color:var(--brown)}
.front-panel-text{left:36px;width:228px;top:80px;text-align:center;font-size:10px;line-height:1.35;color:var(--white)}
.portrait-ring{border-radius:50%;border:4px solid var(--white);background:radial-gradient(circle at 50% 40%,#e9cdbf 0%,#c9a393 40%,#9fb6c8 75%,#7d95ab 100%)}
.front-host{left:11px;top:591px;width:105px;height:105px}
.brand-circle{border-radius:50%;background:var(--blue);border:3px solid var(--white);display:flex;align-items:center;justify-content:center;font-family:"Roboto Condensed","Arial Narrow",sans-serif;font-weight:700;color:var(--white)}
.front-brand{left:405px;top:655px;width:78px;height:78px;font-size:12px}
.contact{text-align:center;font-size:9px;line-height:1.35;color:var(--ink)}
.contact .label{font-weight:700;font-size:13px;color:var(--blue)}
.contact .link{font-weight:700;color:var(--blue)}
.front-contact{left:118px;width:284px;top:654px}
.front-bar{left:216px;top:751px;width:84px;height:6px;background:var(--blue)}

/* back */
.back-base{left:0;top:0;width:511px;height:720px;background:linear-gradient(180deg,#bcd45a 0%,#c9dc55 60%,#d5e25b 100%)}
.back-sheet{left:13px;top:0;width:281px;height:562px;background:var(--white)}
.back-photo{left:294px;top:0;width:217px;height:300px;background:linear-gradient(170deg,#6f9a3f 0%,#a9c66a 35%,#7d86b8 60%,#b8cf62 100%)}
.back-content{left:20px;top:33px;width:270px;height:525px;display:flex;flex-direction:column}
.rule{margin-left:27px;width:217px;height:5px;background:var(--yellow);flex:none}
.back-date{margin-left:24px;margin-top:4px;font-family:"Oswald",sans-serif;font-weight:500;font-size:56px;line-height:1;color:var(--blue);white-space:nowrap}
.back-date small{font-size:29px}
.back-seminar{margin-left:24px;width:225px;text-align:center;font-family:"Oswald",sans-serif;font-weight:200;font-size:42px;line-height:1.1;color:var(--blue);letter-spacing:1px;margin-bottom:6px}
.back-lead{margin-top:12px;font-family:"Roboto Slab",Georgia,serif;font-weight:700;font-size:14.5px;line-height:1.22;color:var(--blue)}
.back-body{margin-top:10px;column-count:2;column-gap:12px;font-size:6px;line-height:1.35;text-align:justify;color:var(--ink)}
.back-h{font-family:"Roboto Slab",Georgia,serif;font-weight:700;font-size:15px;line-height:1.2;color:var(--blue)}
.back-h1{margin-top:12px}
.back-h2{margin-top:14px}
.list-pair{margin-top:8px;display:flex;gap:4px}
.list-pair .bullets{flex:1}
.bullets{list-style:none;font-size:7px;line-height:1.25;color:var(--ink)}
.bullets li{position:relative;padding-left:10px;margin-bottom:3px}
.bullets li::before{content:"";position:absolute;left:0;top:1.5px;width:5px;height:5px;background:var(--blue)}
.back-list-c{margin-top:6px;font-weight:700}
.info-disc{left:290px;top:334px;width:206px;height:206px;border-radius:50%;background:var(--blue);border:4px solid var(--white);color:var(--white);text-align:center}
.info-disc .time{position:absolute;left:0;width:100%;top:40px;font-family:"Oswald",sans-serif;font-weight:300;font-size:13px;text-transform:uppercase;white-space:nowrap}
.info-disc .time b{font-weight:400;font-size:22px}
.info-disc .venue{position:absolute;left:0;width:100%;top:70px;font-family:"Oswald",sans-serif;font-weight:300;font-size:15px;line-height:1.15;text-transform:uppercase}
.info-disc .price{position:absolute;left:0;width:100%;top:106px;font-family:"Oswald",sans-serif;font-weight:500;color:var(--yellow);font-size:18px;white-space:nowrap}
.info-disc .price b{font-size:40px;font-weight:500}
.info-disc .price sup{font-size:16px}
.info-disc .note{position:absolute;left:28px;width:144px;top:160px;font-size:7.2px;line-height:1.3;font-style:italic}
.back-brand{left:304px;top:272px;width:90px;height:90px;font-size:13px}
.back-band{left:0;top:562px;width:511px;height:86px;background:var(--blue)}
.back-band-text{left:190px;top:14px;width:290px;font-family:"Roboto Slab",Georgia,serif;font-weight:700;font-size:8.4px;line-height:1.45;color:var(--white);text-align:justify}
.back-host{left:52px;top:557px;width:120px;height:115px}
.back-contact{left:80px;width:380px;top:655px}
</style>
</head>
<body>
<div class="canvas">

  <section class="flyer flyer--front">
    <div class="front-hero abs" role="img" aria-label="Foto: lächelnde ältere Frau im Profil vor hellem Himmel"></div>
    <h1 class="front-title abs">WECHSELJAHRE –</h1>
    <p class="front-sub abs">HEISS GESCHÜTTELT, NICHT KALT GERÜHRT –</p>

    <div class="front-portrait abs" role="img" aria-label="Foto: fröhliche Frau mit türkisem Schal zeigt Daumen hoch"></div>
    <div class="vol-badge abs">Vol.<b>2</b></div>

    <div class="front-column abs">
      <p class="front-date">23.04.2017</p>
      <p class="front-time">Seminar von <b>9.00 – 15.00</b> Uhr</p>
      <p class="front-venue">Ort: Bildungshaus St. Alwin, 3920 Sorn</p>
      <h2 class="front-lead">Über Abschied, Umbruch, Sinnorientierung und Neuanfang.</h2>
      <p class="front-body">Die Wechseljahre sind keine Krankheit und sie kommen nicht über Nacht. Sie sind eine Einladung an uns Frauen, uns in den vielfältigen Veränderungen, die sich in Körper, Geist und Seele vollziehen, neu zu erfahren. Unsere wahre Schönheit und unser sinnliches Erleben sind von äusseren Dingen unabhängig und blühen gerade im Älterwerden auf eine neue und besondere Weise auf! Das Seminar zeigt auf, in welcher Form uns dabei die Hormone sogar unterstützen.</p>
      <h3 class="front-questions-title">Kennen Sie diese Fragen?</h3>
      <ul class="question-list">
        <li>Wechseljahre, was heisst das für mich?<br>Was passiert gerade mit mir?</li>
        <li>Was möchte ich vom Leben, welche<br>Träume und Wünsche habe ich?</li>
        <li>Was kann ich für mich in dieser Zeit tun?</li>
        <li>Weshalb stelle ich so vieles in Frage und grübele?</li>
        <li>Weshalb kann ich so schlecht<br>einschlafen oder durchschlafen?</li>
        <li>Soll ich Hormone nehmen, was gibt es<br>sonst noch für Möglichkeiten?</li>
      </ul>
    </div>

    <div class="front-panel abs">
      <h2 class="front-panel-title abs">Mit noch mehr Antworten<br>und Tipps für diese<br>spannende Zeit</h2>
      <p class="front-panel-text abs">Ein spannendes Tagesseminar über die Wechselbäder der Gefühle, über Hormone, Orientierung, Hilfen und Möglichkeiten. Über die Zeit davor, mittendrin und danach.</p>
    </div>

    <div class="portrait-ring front-host abs" role="img" aria-label="Porträtfoto der Seminarleiterin"></div>
    <div class="brand-circle front-brand abs">herzwandel</div>

    <div class="contact front-contact abs">
      <p class="label">Anmeldung unter:</p>
      <p class="link">www.wechseljahre-tag.ch / info@herzwandel.ch / 078 / 00 12 345</p>
      <p><b>Mara Lindquist,</b><br>Dipl. Wechseljahresberaterin, Sexualtherapeutin und Mentaltrainerin</p>
      <p class="link">www.herzwandel.ch</p>
    </div>
    <div class="front-bar abs"></div>
  </section>

  <section class="flyer flyer--back">
    <div class="back-base abs"></div>
    <div class="back-photo abs" role="img" aria-label="Foto: Frau sitzt entspannt im sonnigen Gras"></div>
    <div class="back-sheet abs"></div>

    <div class="back-content abs">
      <div class="rule"></div>
      <p class="back-date">23.04.<small>2017.</small></p>
      <p class="back-seminar">SEMINAR</p>
      <div class="rule"></div>

      <h2 class="back-lead">Ein Neuwerden, ein Loslassen, ein einzigartiges Geschenk und Herausforderung zugleich!</h2>
      <p class="back-body">Viele Frauen befinden, dass mit dem Klimakterium eine Last von ihren Schultern fällt. Endlich dürfen sie sich fallen lassen, endlich an sich selbst denken. Für solche Frauen beginnt mit den hormonellen Wallungen eine Phase des Perspektivwechsels. Die Zeit des Klimakteriums lädt zu einer inneren Inventur und gegebenenfalls einer Neuorientierung ein. Statt von einem Gefühlschaos überwältigt zu werden, empfinden sich viele Frauen als emotionell empfindsamer, zugänglicher und berührbarer. Moderatorin und Sängerin Lea Marti nimmt's mit Humor. Sie nennt die Wechseljahre ihren „Inneren Sommer" und träumt von einer implantierten Klimaanlage.</p>

      <h3 class="back-h back-h1">Wenn Sie erfahren möchten,</h3>
      <div class="list-pair">
        <ul class="bullets">
          <li>wie sich Ihr Körper in den Wechseljahren verändert,</li>
          <li>welche Beschwerden dadurch verursacht werden können</li>
        </ul>
        <ul class="bullets">
          <li>was Sie aktiv zur Linderung und Vorbeugung beitragen können,</li>
          <li>wie Sie Ihre eigene Balance und Heilung finden</li>
        </ul>
      </div>

      <h3 class="back-h back-h2">Wollen Sie wissen:</h3>
      <ul class="bullets back-list-c">
        <li>Was mit Ihnen passiert und wie Sie diese neue Lebensphase auf natürliche Weise bewältigen und annehmen können</li>
        <li>Worum es wirklich geht in diesen Jahren</li>
        <li>Wie Sie mutig und lustvoll durch die Wechseljahre kommen</li>
        <li>Mehr wissen über Östrogene, Progesterone und Testosterone</li>
        <li>Dieser Tag macht Mut zum Aufbruch und Neugier auf diese neue Lebensphase. Sie erleben, wie es sein wird, Altes loszulassen, den Blick nach vorn zu richten und wichtige Weichen für Ihren weiteren Lebensweg zu stellen.</li>
      </ul>
    </div>

    <div class="info-disc abs">
      <p class="time">von <b>9.00 – 15.00</b> Uhr</p>
      <p class="venue">Ort: Bildungshaus St.<br>Alwin, 3920 Sorn</p>
      <p class="price">CHF <b>139</b><sup>.00</sup></p>
      <p class="note">Kosten Seminar inkl. Getränke, Obst, Z'Nüni und 4 Gang Mittags Menü.</p>
    </div>
    <div class="brand-circle back-brand abs">herzwandel</div>

    <div class="back-band abs">
      <p class="back-band-text abs">Dieser Tag macht Mut zum Aufbruch und Neugier auf diese neue Lebensphase. Sie erleben, wie es sein wird, Altes loszulassen, den Blick nach vorn zu richten und wichtige Weichen für Ihren weiteren Lebensweg zu stellen.</p>
    </div>
    <div class="portrait-ring back-host abs" role="img" aria-label="Porträtfoto der Seminarleiterin"></div>

    <div class="contact back-contact abs">
      <p class="label">Anmeldung unter:</p>
      <p class="link">www.wechseljahre-tag.ch / info@herzwandel.ch / 078 / 00 12 345</p>
      <p><b class="link">Mara Lindquist</b>, Dipl. Wechseljahresberaterin, Sexualtherapeutin und Mentaltrainerin</p>
      <p class="link">www.herzwandel.ch</p>
    </div>
  </section>

</div>
</body>
</html>
```